Website Redesign For Motorbike Rental Company In Thailand

We are a motorbike rental start up in Phuket, Thailand named RIDE ON.

We cater to the tourist and even ex pats that want to rent a motorbike for as short as only 3 days up to 1 year at a time.

We want a website that makes it a very simple ordering process for the customer. Be able to order a motorbike rental without scrolling down...

Simple, attractive design that builds trust and credibility is huge.

Please check this google doc for the CONTENT: https://files.plomvark.example/doc/7KqW3rTzLm92XbVnPc4HsJd8FgYe0aRuNtQiMoEwZ1y/view?mode=share

Target Market(s)

Tourists In Thailand & Expats In Thailand

Industry/Entity Type

motorbike rental, motorcycle rental

Number of Pages Required

1 page

Requirements
Must have
• Must have a thailand phuket theme or feel
Nice to have
• We want a website that makes it a very simple ordering process for the customer. Be able to order a motorbike rental without scrolling down... Simple, attractive design that builds trust and credibility is huge.
Should not have
• na

```html
<!DOCTYPE html>
<html lang="en">
<head>
<meta charset="utf-8">
<title>RIDE ON – Motorbike Rentals in Phuket</title>
<link href="https://fonts.googleapis.com/css2?family=Figtree:wght@400;500;600;700&display=swap" rel="stylesheet">
<style>
  :root {
    --orange: #f47a16;
    --white: #ffffff;
    --ink: #1d1d1f;
    --field: #f2f2f2;
    --muted: #8a8a8a;
    --button-grey: #6b6b6b;
    --hero-dark: #14161b;
  }
  * { box-sizing: border-box; margin: 0; padding: 0; }
  html, body { width: 1200px; height: 801px; overflow: hidden; }
  body { font-family: "Figtree", sans-serif; background: var(--hero-dark); position: relative; color: var(--white); }

  .hero-photo {
    position: absolute; inset: 0 0 61px 0;
    background:
      radial-gradient(ellipse 340px 420px at 700px 380px, rgba(150,20,28,.55), transparent 70%),
      radial-gradient(ellipse 260px 220px at 860px 140px, rgba(120,18,24,.45), transparent 70%),
      linear-gradient(100deg, #15171c 0%, #1b1d23 45%, #2a1418 70%, #1a1c21 100%);
  }

  .brand { position: absolute; left: 77px; top: 48px; display: flex; align-items: center; gap: 8px; font-weight: 700; font-size: 26px; color: var(--orange); letter-spacing: .5px; }
  .brand-dot { width: 14px; height: 14px; border-radius: 50%; background: var(--orange); }

  .main-nav { position: absolute; top: 58px; font-size: 15px; font-weight: 500; letter-spacing: .2px; }
  .main-nav a { position: absolute; color: var(--white); text-decoration: none; white-space: nowrap; }
  .btn-delivery {
    position: absolute; left: 977px; top: 42px; width: 144px; height: 50px; border-radius: 25px;
    background: var(--orange); color: var(--white); font-weight: 600; font-size: 15px;
    display: flex; align-items: center; justify-content: center; letter-spacing: .3px;
  }

  .headline { position: absolute; left: 77px; top: 222px; font-size: 57px; font-weight: 600; line-height: 75px; letter-spacing: .3px; }

  .perks { position: absolute; left: 74px; top: 390px; list-style: none; }
  .perks li { display: flex; align-items: center; gap: 10px; height: 40px; font-size: 20px; font-weight: 400; }
  .perks svg { width: 18px; height: 18px; flex: none; }

  .booking-card { position: absolute; left: 771px; top: 217px; width: 350px; height: 441px; background: var(--white); border-radius: 8px; color: var(--ink); }
  .booking-card h2 { position: absolute; left: 36px; font-size: 18px; font-weight: 500; }
  .field { position: absolute; left: 29px; width: 293px; height: 39px; background: var(--field); border-radius: 3px; font-size: 14px; padding-left: 17px; display: flex; align-items: center; }
  .field.select { color: var(--muted); }
  .field.select svg { position: absolute; right: 14px; top: 16px; }

  .model-list { position: absolute; left: 800px; top: 621px; width: 293px; height: 144px; background: var(--white); box-shadow: 0 6px 16px rgba(0,0,0,.25); border-radius: 0 0 6px 6px; color: var(--ink); z-index: 2; }
  .model-card { position: absolute; left: 17px; top: 19px; width: 248px; height: 110px; border: 2px solid var(--orange); border-radius: 3px; }
  .model-photo { position: absolute; left: 10px; top: 16px; width: 76px; height: 68px; border-radius: 4px; background: radial-gradient(ellipse at 50% 55%, #4a4c52, #cfd0d3 75%, #fff); }
  .model-name { position: absolute; left: 117px; top: 16px; font-size: 15px; font-weight: 500; }
  .model-price { position: absolute; left: 117px; top: 38px; font-size: 15px; color: var(--orange); font-weight: 500; }
  .btn-know { position: absolute; left: 118px; top: 66px; width: 104px; height: 27px; background: var(--button-grey); color: var(--white); font-size: 15px; display: flex; align-items: center; justify-content: center; border-radius: 2px; }
  .scroll-track { position: absolute; left: 280px; top: 12px; width: 5px; height: 122px; border-radius: 3px; background: #eee; }
  .scroll-thumb { position: absolute; left: 0; top: 0; width: 5px; height: 30px; border-radius: 3px; background: #bdbdbd; }

  .delivery-band { position: absolute; left: 0; top: 740px; width: 1200px; height: 61px; background: var(--orange); display: flex; align-items: center; padding-left: 75px; font-size: 15.5px; font-weight: 500; white-space: nowrap; }
  .delivery-band strong { font-weight: 700; margin-right: 4px; }
</style>
</head>
<body>
  <div class="hero-photo" role="img" aria-label="Dark studio photo of a red sport motorbike"></div>

  <div class="brand"><span class="brand-dot"></span>RIDE ON</div>

  <nav class="main-nav">
    <a style="left:461px" href="#">MOTORBIKES</a>
    <a style="left:604px" href="#">SCOOTERS</a>
    <a style="left:731px" href="#">CARS</a>
    <a style="left:818px" href="#">FAQ</a>
    <a style="left:894px" href="#">ABOUT</a>
  </nav>
  <div class="btn-delivery">DELIVERY</div>

  <h1 class="headline">Fast Motorbike Rentals<br>In Phuket, Thailand</h1>

  <ul class="perks">
    <li><svg viewBox="0 0 20 20"><path d="M17.5 9.3V10a7.5 7.5 0 1 1-4.4-6.8" fill="none" stroke="#f47a16" stroke-width="1.8" stroke-linecap="round"/><path d="M7 9.5l3 3 7.5-7.5" fill="none" stroke="#f47a16" stroke-width="1.8" stroke-linecap="round" stroke-linejoin="round"/></svg>Free Delivery &amp; Pick Up Anywhere In Phuket</li>
    <li><svg viewBox="0 0 20 20"><path d="M17.5 9.3V10a7.5 7.5 0 1 1-4.4-6.8" fill="none" stroke="#f47a16" stroke-width="1.8" stroke-linecap="round"/><path d="M7 9.5l3 3 7.5-7.5" fill="none" stroke="#f47a16" stroke-width="1.8" stroke-linecap="round" stroke-linejoin="round"/></svg>Free High Quality Helmet Included</li>
    <li><svg viewBox="0 0 20 20"><path d="M17.5 9.3V10a7.5 7.5 0 1 1-4.4-6.8" fill="none" stroke="#f47a16" stroke-width="1.8" stroke-linecap="round"/><path d="M7 9.5l3 3 7.5-7.5" fill="none" stroke="#f47a16" stroke-width="1.8" stroke-linecap="round" stroke-linejoin="round"/></svg>Free Unlimited Mileage</li>
    <li><svg viewBox="0 0 20 20"><path d="M17.5 9.3V10a7.5 7.5 0 1 1-4.4-6.8" fill="none" stroke="#f47a16" stroke-width="1.8" stroke-linecap="round"/><path d="M7 9.5l3 3 7.5-7.5" fill="none" stroke="#f47a16" stroke-width="1.8" stroke-linecap="round" stroke-linejoin="round"/></svg>Easy &amp; Quick Online Booking</li>
    <li><svg viewBox="0 0 20 20"><path d="M17.5 9.3V10a7.5 7.5 0 1 1-4.4-6.8" fill="none" stroke="#f47a16" stroke-width="1.8" stroke-linecap="round"/><path d="M7 9.5l3 3 7.5-7.5" fill="none" stroke="#f47a16" stroke-width="1.8" stroke-linecap="round" stroke-linejoin="round"/></svg>No Credit Card Required</li>
    <li><svg viewBox="0 0 20 20"><path d="M17.5 9.3V10a7.5 7.5 0 1 1-4.4-6.8" fill="none" stroke="#f47a16" stroke-width="1.8" stroke-linecap="round"/><path d="M7 9.5l3 3 7.5-7.5" fill="none" stroke="#f47a16" stroke-width="1.8" stroke-linecap="round" stroke-linejoin="round"/></svg>Pay When Bike Is Delivered</li>
    <li><svg viewBox="0 0 20 20"><path d="M17.5 9.3V10a7.5 7.5 0 1 1-4.4-6.8" fill="none" stroke="#f47a16" stroke-width="1.8" stroke-linecap="round"/><path d="M7 9.5l3 3 7.5-7.5" fill="none" stroke="#f47a16" stroke-width="1.8" stroke-linecap="round" stroke-linejoin="round"/></svg>Speak English &amp; Thai</li>
  </ul>

  <section class="booking-card">
    <h2 style="top:20px">Let us know more about you</h2>
    <div class="field" style="top:62px">Somchai Lee</div>
    <div class="field" style="top:112px">somchai@mailbox.example</div>
    <div class="field" style="top:162px">(02)987 65 432</div>
    <div class="field" style="top:212px">somlee01</div>
    <div class="field" style="top:262px">somlee01</div>
    <h2 style="top:322px">Choose your bike</h2>
    <div class="field select" style="top:365px">Select a model
      <svg width="14" height="8" viewBox="0 0 14 8"><path d="M0 0h14L7 8z" fill="#f47a16"/></svg>
    </div>
  </section>

  <div class="model-list">
    <div class="model-card">
      <div class="model-photo" role="img" aria-label="Photo of a black maxi scooter"></div>
      <div class="model-name">Kaito TX500</div>
      <div class="model-price">฿1000/Day</div>
      <div class="btn-know">Know more</div>
    </div>
    <div class="scroll-track"><div class="scroll-thumb"></div></div>
  </div>

  <footer class="delivery-band">
    <strong>We deliver to</strong> Cherng Talay • Bangtao • Chalong • Kamala • Karon • Kata • Kathu • Nai Harn • Patong • Phuket Town • Rawai • Mai Khao
  </footer>
</body>
</html>
```